We need to redesign the app icon and splash screen for our app called "Rotation Ledger". The app records the amount of bench-time and game-time for each player in a team. The target of the app is a quantitative measure of the participation in the game by the players in a team. The app is available on Appvault.

The app can be used by coaches to make sure all players get an equal amount of game-time and by parents to make sure their children get a fair go.

The app is a universal iOS app (iPhone 4,5 and iPad) so the splash screen needs to suit multiple resolutions in both portrait and landscape.

Thank you all for submitting designs. They are all very good and it is quite hard to decide amongst your good designs.

We are going through them all this afternoon and we will select the design we will move forward with.

Once again thank you

regards

Colin Feeney

Target Market(s)

Parents of children at school, teachers, coaches, team managers

Industry/Entity Type

Landscape

Requirements
Must have
• app icon 1024x1024

Splash Screens in both portrait and landscape a version for each of these resolutions (the splash screen must have two buttons (Get Started and Introduction)

iPhone
320x480, 640x960, 640x1136

iPad
1536x2048, 768x1024

```html
<!DOCTYPE html>
<html lang="en">
<head>
<meta charset="utf-8">
<title>Rotation Ledger – Splash Screen and App Icon</title>
<link rel="stylesheet" href="https://fonts.googleapis.com/css2?family=Arvo:wght@700&family=Arimo:wght@700&display=swap">
<style>
  :root {
    --backdrop-light: #f4f4f4;
    --backdrop-dark: #8c8c8c;
    --royal-blue: #1746d6;
    --deep-blue: #0a2a9e;
    --sky-blue: #3f7cf0;
    --white: #ffffff;
    --green-top: #6fe04a;
    --green-bottom: #1d8f12;
    --red-top: #f2454a;
    --red-bottom: #a50d12;
    --figure-tone: #dfe6f5;
  }
  html, body {
    margin: 0;
    padding: 0;
    overflow: hidden;
  }
  body {
    width: 1200px;
    height: 1000px;
    position: relative;
    background: radial-gradient(ellipse at 55% 45%, var(--backdrop-light) 0%, #d8d8d8 60%, var(--backdrop-dark) 100%);
  }

  /* Brand mark: plain ring with the name set inside */
  .brand-mark {
    position: absolute;
    box-sizing: border-box;
    border-radius: 50%;
    border: 12px solid var(--white);
    display: flex;
    flex-direction: column;
    align-items: center;
    justify-content: center;
    font-family: "Arvo", serif;
    font-weight: 700;
    color: var(--white);
    line-height: 1.15;
    text-align: center;
  }

  /* Splash screen */
  .splash {
    position: absolute;
    left: 170px;
    top: 165px;
    width: 376px;
    height: 667px;
    overflow: hidden;
    background: linear-gradient(160deg, var(--sky-blue) 0%, var(--royal-blue) 45%, var(--deep-blue) 100%);
  }
  .splash__mark {
    left: 94px;
    top: 100px;
    width: 190px;
    height: 190px;
    font-size: 24px;
    letter-spacing: 1px;
  }
  .splash__title {
    position: absolute;
    left: 0;
    top: 302px;
    width: 100%;
    margin: 0;
    text-align: center;
    font-family: "Arvo", serif;
    font-weight: 700;
    font-size: 20px;
    letter-spacing: 1px;
    color: var(--white);
  }
  .splash__button {
    position: absolute;
    left: 70px;
    width: 241px;
    height: 61px;
    border-radius: 14px;
    display: flex;
    align-items: center;
    justify-content: center;
    font-family: "Arimo", sans-serif;
    font-weight: 700;
    font-size: 27px;
    letter-spacing: 0.5px;
    color: var(--white);
    text-shadow: 0 1px 2px rgba(0,0,0,0.35);
    box-shadow: 0 3px 5px rgba(0,0,0,0.4), inset 0 1px 0 rgba(255,255,255,0.5);
  }
  .splash__button--intro {
    top: 372px;
    background: linear-gradient(180deg, var(--green-top) 0%, #3bbd22 50%, var(--green-bottom) 100%);
  }
  .splash__button--start {
    top: 451px;
    background: linear-gradient(180deg, var(--red-top) 0%, #d9222a 50%, var(--red-bottom) 100%);
  }
  .splash__players {
    position: absolute;
    left: 64px;
    top: 536px;
    width: 172px;
    height: 70px;
    border-radius: 8px;
    background: linear-gradient(180deg, rgba(223,230,245,0.25), rgba(223,230,245,0.55));
  }
  .splash__field {
    position: absolute;
    left: 0;
    bottom: 0;
  }

  /* App icon */
  .app-icon {
    position: absolute;
    left: 710px;
    top: 337px;
    width: 323px;
    height: 326px;
    border-radius: 18px;
    overflow: hidden;
    background: linear-gradient(180deg, #5a7cf0 0%, #2a4fe6 38%, #0d36d8 55%, #0a2fc4 100%);
    box-shadow: 0 4px 6px rgba(0,0,0,0.45);
  }
  .app-icon__sheen {
    position: absolute;
    left: -40px;
    top: -150px;
    width: 420px;
    height: 290px;
    border-radius: 50%;
    background: linear-gradient(180deg, rgba(255,255,255,0.45), rgba(255,255,255,0.08));
  }
  .app-icon__mark {
    left: 72px;
    top: 100px;
    width: 180px;
    height: 180px;
    font-size: 23px;
    letter-spacing: 1px;
  }
</style>
</head>
<body>

  <main class="splash" aria-label="Rotation Ledger splash screen">
    <div class="brand-mark splash__mark" aria-hidden="true"><span>ROTATION</span><span>LEDGER</span></div>
    <h1 class="splash__title">ROTATION LEDGER</h1>
    <div class="splash__button splash__button--intro">Introduction</div>
    <div class="splash__button splash__button--start">Get Started</div>
    <div class="splash__players" role="img" aria-label="Silhouettes of two children playing football"></div>
    <svg class="splash__field" width="376" height="80" viewBox="0 0 376 80" aria-hidden="true">
      <path d="M0 55 C 120 42, 250 26, 376 12 L376 80 L0 80 Z" fill="var(--white)"/>
    </svg>
  </main>

  <div class="app-icon" role="img" aria-label="Rotation Ledger app icon">
    <div class="app-icon__sheen"></div>
    <div class="brand-mark app-icon__mark" aria-hidden="true"><span>ROTATION</span><span>LEDGER</span></div>
  </div>

</body>
</html>
```